The First Annual Fernwick Legacy Gala

Something similar to the attached but an attention grabber. It needs to attract people with money to spend!

```html
<!DOCTYPE html>
<html lang="en">
<head>
<meta charset="utf-8">
<title>The First Annual Fernwick Legacy Gala</title>
<link href="https://fonts.googleapis.com/css2?family=Noto+Serif:wght@700&family=Montserrat:wght@400;500;700&family=Tinos:ital,wght@0,700;1,400&display=swap" rel="stylesheet">
<style>
  :root {
    --backdrop: #4a4a4a;
    --sky-top: #1f63c4;
    --sky-mid: #5d97da;
    --sky-low: #b9d3ee;
    --lawn: #7f8d55;
    --coral: #f45f5e;
    --lavender: #c6c9fb;
    --periwinkle: #8f95e8;
    --trim: #6f6b4b;
    --paper: #ffffff;
    --paper-shade: #e6e6e6;
    --ink: #1c1c1c;
    --white: #ffffff;
    --date-bar: rgba(60, 66, 80, 0.82);
  }
  * { margin: 0; padding: 0; box-sizing: border-box; }
  html, body { width: 990px; height: 1200px; overflow: hidden; background: var(--backdrop); }
  .flyer {
    position: absolute; left: 45px; top: 18px; width: 900px; height: 1164px;
    overflow: hidden; isolation: isolate;
    background: linear-gradient(160deg, var(--paper) 30%, var(--paper-shade) 60%, var(--paper) 85%);
  }
  .hero-photo {
    position: absolute; left: 0; top: 0; width: 900px; height: 740px;
    background: linear-gradient(180deg, var(--sky-top) 0%, var(--sky-mid) 32%, var(--sky-low) 52%, #e9edf2 66%, #cfd3d8 78%, var(--lawn) 90%);
  }
  .waves { position: absolute; left: 0; top: 0; }
  .presenter {
    position: absolute; top: 56px; left: 0; width: 900px; text-align: center;
    font: 500 17px/1 "Montserrat", sans-serif; color: var(--white); letter-spacing: 0.3px;
  }
  .presenter-rule { position: absolute; left: 74px; top: 86px; width: 751px; height: 1px; background: rgba(255,255,255,0.85); }
  .event-title {
    position: absolute; top: 96px; left: 0; width: 900px; text-align: center;
    font: 700 58px/74px "Noto Serif", serif; color: var(--white);
  }
  .date-bar {
    position: absolute; left: 90px; top: 247px; width: 720px; height: 42px;
    background: var(--date-bar); color: var(--white); text-align: center;
    font: 700 19.5px/42px "Montserrat", sans-serif; letter-spacing: 0.2px;
  }
  .headline {
    position: absolute; left: 72px; top: 618px; width: 400px;
    font: 700 36px/41px "Noto Serif", serif; color: var(--coral);
  }
  .story { position: absolute; left: 72px; top: 760px; width: 368px; }
  .story p { font: italic 400 17px/19.8px "Tinos", serif; color: var(--ink); margin-bottom: 7px; }
  .follow-note {
    position: absolute; left: 72px; top: 1055px; width: 335px;
    font: 700 19px/23px "Tinos", serif; color: var(--white);
  }
  .ticket-info { position: absolute; left: 508px; top: 693px; width: 322px; }
  .ticket-info p { font: 700 17px/22px "Montserrat", sans-serif; color: var(--coral); text-transform: uppercase; margin-bottom: 13px; }
  .tag {
    position: absolute; left: 508px; width: 334px; height: 30px;
    border-bottom: 1px solid var(--periwinkle);
  }
  .tag-label {
    display: block; width: 235px; height: 29px; padding-left: 15px;
    background: var(--periwinkle); clip-path: polygon(0 0, 218px 0, 235px 100%, 0 100%);
    font: 700 20px/29px "Tinos", serif; color: var(--white);
  }
  .tag-tickets { top: 851px; }
  .tag-contacts { top: 1024px; }
  .outlets { position: absolute; left: 523px; top: 890px; width: 320px; }
  .outlet { margin-bottom: 5px; font: 400 14px/18px "Montserrat", sans-serif; color: var(--ink); }
  .outlet strong { font-weight: 700; display: block; }
  .contacts { position: absolute; left: 508px; top: 1063px; font: 500 17px/26px "Montserrat", sans-serif; color: var(--ink); }
  .contacts span { display: inline-block; width: 164px; }
</style>
</head>
<body>
<main class="flyer">
  <div class="hero-photo" role="img" aria-label="Photo of the white clapboard community center with a metal roof, trees and lawn under a blue cloudy sky"></div>

  <svg class="waves" width="900" height="1164" viewBox="0 0 900 1164" aria-hidden="true">
    <path d="M0 760 L0 606 C 180 560 380 600 520 640 C 640 672 760 640 900 610 L900 760 Z" fill="#f3f3f3"/>
    <path d="M0 524 C 120 470 300 490 480 585 L 0 610 Z" fill="var(--coral)"/>
    <path d="M0 598 C 140 545 300 560 470 615 C 590 655 700 690 780 660 C 840 640 880 600 900 528 L900 615 C 760 700 640 690 520 650 C 380 605 200 570 0 610 Z" fill="var(--lavender)"/>
    <path d="M0 598 C 140 545 300 560 470 615" fill="none" stroke="var(--trim)" stroke-width="3"/>
    <path d="M0 610 C 200 570 380 605 520 650 C 640 690 760 700 900 615" fill="none" stroke="var(--trim)" stroke-width="3"/>
    <path d="M0 1063 C 90 1025 200 1005 300 1020 C 450 1045 580 1150 720 1156 C 800 1158 860 1120 900 1084 L900 1164 L0 1164 Z" fill="var(--coral)"/>
  </svg>

  <div class="presenter">THE FERNWICK COMMUNITY CENTER PRESENTS</div>
  <div class="presenter-rule"></div>
  <h1 class="event-title">The First Annual Fernwick<br>Legacy Gala</h1>
  <div class="date-bar">APRIL 23, 2022 STARTING AT 5:00 PM WITH COCKTAIL HOUR</div>

  <h2 class="headline">Live auction,<br>silent auction, raffle<br>and a cash bar!</h2>

  <div class="story">
    <p>Come on out to the Fernwick Community Center for a delicious prime rib dinner, drinks, entertainment and more! There will be plenty of amazing auction items for everyone to choose from.</p>
    <p>All proceeds will go to the Fernwick Community Center. We will share some history of the school and each year we will highlight a local family. This year will be the Harlow family who have been here for 135 years!!</p>
    <p>High side barn, dirt bike, custom knives, a guided fishing trip, and so much more!</p>
  </div>

  <p class="follow-note">Follow the Fernwick Community Center's online page to see all the auction items available!</p>

  <div class="ticket-info">
    <p>Tickets for the event are $50 each or $90 for a couple</p>
    <p>Tickets for the 10x12 high side barn $25 each or 5 for $100. Donated by: Ridgeline Shed Company of Alder Falls.</p>
  </div>

  <div class="tag tag-tickets"><span class="tag-label">Get your tickets from:</span></div>

  <div class="outlets">
    <div class="outlet"><strong>Ridgeline Shed Company in Alder Falls</strong>42 Cedar Mill Rd, Alder Falls</div>
    <div class="outlet"><strong>Summit Peak Realty</strong>218 W Aspen St, Alder Falls</div>
    <div class="outlet"><strong>Fernwick General Store</strong>6150 Route 44, Fernwick</div>
  </div>

  <div class="tag tag-contacts"><span class="tag-label">Or get them from</span></div>

  <div class="contacts">
    <div><span>Dana Whitlock -</span>(555)210-4378</div>
    <div><span>Jolene Marsh -</span>(555)382-9164</div>
  </div>
</main>
</body>
</html>
```